Power Point Template Kalvoren sustainability consulting

Please note:
We are not looking for new design proposals anymore since we've already received templetes from two designers that we really like. We are currently discussing possible changes with them and will make a final decision soon. Thank you very much.

(find english description below)
We are a small German start-up that offers sustainability consulting. For presentations of results, our company presentation, proposals, lectures, etc., we need a PowerPoint template that matches our logo. We come from classic management consulting / strategy consulting and also deal with facts and figures in sustainability consulting. Therefore, the template should not be too fancy and should not only consist of photos. But it shouldn't be a completely sober template either. Our logo with the green leaves for sustainability (three leaves for KALvoren) and the white bar chart (with the dynamic swing upwards) reflects our attitude well, where we see ourselves on the range from playful to sober and classic to modern.

It might be nice for the template to include the shape of one of the leaves (from the logo). Also, the logo should appear in a corner of each slide. The colors from the logo (see appendix) should be partially reflected in the presentation. We can also imagine a gold-brown tone (see website www.kalvoren-consulting.example) or a coral tone as a contrast. (Attention - the website is not final yet).

For a first suggestion, it is sufficient to suggest three to four slides (cover sheet, chapter/separation slide, text slide, data slide). We will then mark drafts that we like. In total, we would then need about 6-10 more slide templates, e.g. about us, team, slide for a statement, 2-3 data charts (pie, bar, column), top 3 - 5 list, timeline, contact (more slides are welcome ).

We are a small German start-up offering sustainability consulting. We need a power point template for result presentations, our company presentation, proposals, lectures etc. The template should be aligned with our logo. Our background lies in classic management consulting / strategy consulting and we also deal with facts and figures in sustainability consulting. Therefore, the template should not be too playful and not only consist of photos. But it should also not be a completely clear template. Our logo with the green leaves for sustainability (three leaves for KALvoren) and the white bar chart (with the dynamic upward swing) reflects our attitude well, where we see ourselves on the range from playful to down-to-earth and classic to modern .

For the template, it might be nice to incorporate the shape of one of the leaves (from the logo). Also, the logo should show up in one corner on each slide. Some of the colors from the logo (see attachment) should be reflected in the presentation. We could also think of a gold-brown tone (see website www.kalvoren-consulting.example) or a coral tone for contrast. (Attention - the website is not final yet).

For a first proposal it is quite sufficient to suggest us three to four slides (cover page, chapter/separation slide, text slide, data slide). We will then mark the drafts that we like. In total we would need about 6-10 more slide templates, eg About us, Team, slide for a statement, 2-3 data charts (pie, bar, column), Top 3 - 5 List, Timeline, Contact (more slides are welcome).

Target Market(s)

Corporations, large companies and SMEs

Industry/Entity Type

Unternehmensberatung, Nachhaltigkeitsberatung

Font styles to use
Sans Serif
Other font styles liked:
• Calibri

Colors
00AB8E
00BBA5
67D7C9
C6EFE9
E9F9F6

Requirements
Must have
• see description (e.g. the colors of our logo)
Nice to have
• see description (e.g. elements of the logo included)
Should not have
• see description

```html
<!DOCTYPE html>
<html lang="en">
<head>
<meta charset="utf-8">
<title>Kalvoren – Presentation Template</title>
<link rel="stylesheet" href="https://fonts.googleapis.com/css2?family=Alegreya+Sans:wght@300;400;500;700&display=swap">
<style>
:root{
  --green-dark:#3d7a1c;
  --green-mid:#6d9f2c;
  --green-light:#a9c84a;
  --green-pale:#d3e38a;
  --green-wash:#eef3de;
  --grey-text:#5e5e5e;
  --grey-soft:#8a8a8a;
  --grey-line:#d9d9d9;
  --chart-grey:#6d7072;
  --stage:#c4c4c4;
  --white:#ffffff;
  --font:"Alegreya Sans",Calibri,sans-serif;
}
*{box-sizing:border-box;margin:0;padding:0}
html,body{width:1200px;height:2203px;overflow:hidden}
body{background:var(--stage);font-family:var(--font);color:var(--grey-text);position:relative}

/* slide frame */
.slide{position:absolute;width:359px;height:201px;background:var(--white);overflow:hidden}
.hero{left:161px;top:170px;transform:scale(2.4457);transform-origin:0 0}
.slide > *{position:absolute}

/* brand */
.brand{display:flex;align-items:center;gap:3px;color:#6a6a6a;font-weight:400;line-height:1}
.brand i{display:block;border-radius:50%;background:var(--green-mid)}
.brand-lg{left:28px;top:28px;font-size:13px}
.brand-lg i{width:9px;height:9px}
.brand-sub{font-size:3.4px;letter-spacing:.3px;color:var(--grey-soft);position:absolute;left:62px;top:43px}

.cover-title{left:28px;top:74px;font-size:19px;line-height:1.12;font-weight:500;color:var(--green-dark);letter-spacing:-.2px}
.cover-subtitle{left:28px;top:123px;font-size:6.6px;font-weight:300;color:var(--grey-text)}
.url-pill{left:28px;top:148px;width:70px;height:9px;border-radius:5px;background:var(--green-dark);color:var(--white);font-size:3.4px;display:flex;align-items:center;justify-content:center}
.copyright-strip{left:0;bottom:0;width:100%;height:9px;background:#f2f2f2;font-size:2.6px;letter-spacing:.7px;color:#8a8a8a;display:flex;align-items:center;justify-content:center}
.deco{right:0;top:0;width:200px;height:201px}

/* photo placeholders */
.photo-field{left:0;top:0;width:100%;height:100%;background:linear-gradient(120deg,#f4f6ec 0%,#dfe9c8 45%,#c9d9a3 70%,#efe2b6 100%);opacity:.9}
.photo-leaves{background:linear-gradient(135deg,#3f5524 0%,#7f9650 45%,#d7d09a 80%,#efe4b5 100%)}
.photo-landscape{background:linear-gradient(180deg,#b6c8b0 0%,#7c9a72 35%,#4c6b44 70%,#3a5733 100%)}
.photo-team{background:linear-gradient(100deg,#4d7c22 0%,#7aa63a 55%,#c8d98c 100%)}
.portrait{background:linear-gradient(180deg,#dcdcd8 0%,#b9b4ac 60%,#8e8a86 100%)}

/* content slide chrome */
.edge-accent{left:0;top:10px;width:3px;height:11px;background:var(--green-light)}
.slide-title{left:17px;top:9px;font-size:12.5px;font-weight:300;color:var(--green-mid);white-space:nowrap}
.slide-title b{font-weight:500;color:var(--green-dark)}
.slide-footer{left:0;top:179px;width:100%;height:22px}
.slide-footer > *{position:absolute}
.mini-brand{left:8px;top:5px;font-size:6px;color:#777;display:flex;align-items:center;gap:2px}
.mini-brand i{width:3.5px;height:3.5px;border-radius:50%;background:var(--green-mid);display:block}
.footer-bar{left:48px;top:6px;width:293px;height:2.6px;border-radius:2px;background:linear-gradient(90deg,var(--green-dark),var(--green-mid) 55%,var(--green-pale))}
.footer-note{left:255px;top:1.5px;font-size:1.9px;color:var(--grey-soft);white-space:nowrap}
.page-no{left:341px;top:4px;width:7px;height:7px;border-radius:50%;background:var(--green-dark);color:var(--white);font-size:3px;display:flex;align-items:center;justify-content:center}

/* text */
.body-text{font-size:2.6px;line-height:1.4;color:var(--grey-text)}
.body-text p+p{margin-top:3px}
.bullets{font-size:2.4px;line-height:1.4;color:var(--grey-text);list-style:none}
.bullets li{position:relative;padding-left:4px;margin-bottom:2px}
.bullets li::before{content:"";position:absolute;left:0;top:1.2px;width:1.3px;height:1.3px;border-radius:50%;background:var(--green-dark)}
.bullets.on-dark{color:var(--white)}
.bullets.on-dark li::before{background:var(--white)}
.subhead{font-size:5.2px;font-weight:500;color:var(--green-dark)}

/* about */
.about-photo{left:15px;top:47px;width:170px;height:120px}
.about-callout{left:194px;top:47px;width:150px;height:28px;border-radius:2px;background:var(--green-dark);color:var(--white);font-size:2.7px;line-height:1.35;padding:4px 5px 4px 32px}
.about-callout::before{content:"";position:absolute;left:6px;top:6px;width:16px;height:16px;border-radius:50%;background:rgba(255,255,255,.25)}

/* heading + photo band */
.band-photo{left:0;top:47px;width:359px;height:118px}
.band-box{left:202px;top:0;width:145px;height:156px;background:var(--green-dark);padding:62px 10px 0 14px}

/* team */
.team-band{left:0;top:0;width:359px;height:45px}
.team-title{left:17px;top:12px;font-size:12.5px;font-weight:300;color:var(--white)}
.team-title b{font-weight:500}
.member{top:44px;width:100px;text-align:center}
.member .portrait{width:66px;height:66px;margin:0 auto 6px}
.member h3{font-size:4.6px;font-weight:500;color:var(--green-dark)}
.member .role{font-size:2.6px;color:var(--grey-soft);margin:1px 0 3px}
.member p{font-size:2.5px;line-height:1.35;padding:0 14px}

/* cards */
.card{top:62px;width:90px;height:115px;border-radius:5px;padding:14px 9px 0;text-align:center;color:var(--white)}
.card h3{font-size:5.2px;font-weight:500;line-height:1.05;margin-bottom:6px}
.card p{font-size:2.6px;line-height:1.35}
.card.dark{background:var(--green-dark)}
.card.mid{background:#b3d06a}
.card.light{background:#d6e78c}
.card::after{content:"";position:absolute;right:6px;top:-6px;width:12px;height:12px;border-radius:50%;background:var(--green-mid);border:1.5px solid var(--white)}

/* timeline */
.tl-line{left:0;top:68px;width:359px;border-top:.6px dashed #c7c7c7}
.tl-item{top:57px;width:48px;text-align:center}
.tl-year{font-size:3.6px;color:var(--grey-text);height:9px}
.tl-dot{width:2.5px;height:2.5px;background:var(--green-dark);margin:0 auto 6px}
.tl-icon{width:17px;height:17px;border-radius:50%;margin:0 auto 4px;display:flex;align-items:center;justify-content:center}
.tl-icon.dark{background:var(--green-dark)}
.tl-icon.light{background:var(--green-light)}
.tl-icon.ring{border:1.4px solid var(--green-pale)}
.tl-item h3{font-size:3.4px;font-weight:400;line-height:1.1;color:#555;margin-bottom:4px}
.tl-item p{font-size:2.3px;line-height:1.35;padding:0 3px}

/* section break */
.section-title{left:28px;top:86px;font-size:18px;font-weight:500;color:var(--green-dark)}
.section-text{left:28px;top:111px;width:130px;font-size:3.4px;line-height:1.35;color:var(--grey-text)}

/* donuts */
.donut{top:48px;width:70px;text-align:center}
.donut svg{width:48px;height:48px;display:block;margin:0 auto 8px}
.donut h3{font-size:3.6px;font-weight:500;color:var(--green-dark);margin-bottom:3px}
.donut p{font-size:2.4px;line-height:1.35}

/* bar charts */
.bar-chart{top:56px;width:140px}
.bar-row{display:flex;align-items:center;height:10px}
.bar-row span{font-size:2.2px;color:var(--grey-soft);width:24px}
.bar-row .seg{height:4px}
.seg.a{background:var(--green-dark)}
.seg.b{background:var(--green-light)}
.seg.c{background:var(--chart-grey)}
.bar-axis{display:flex;justify-content:space-between;padding-left:24px;font-size:2px;color:var(--grey-soft);margin-top:2px}
.chart-note{top:135px;width:140px}
.chart-note h3{font-size:3.6px;font-weight:500;color:var(--green-dark);margin-bottom:2px}

/* 3d-style pie */
.pie-wrap{left:112px;top:66px;width:135px;height:80px}
.pie-side{position:absolute;left:0;top:14px;width:135px;height:62px;border-radius:50%;background:linear-gradient(90deg,#2c5a12,#5d8a25 50%,#8aae32)}
.pie-top{position:absolute;left:0;top:0;width:135px;height:62px;border-radius:50%;background:conic-gradient(var(--green-mid) 0 72deg,#c8dd6a 72deg 202deg,#5b6a4a 202deg 245deg,var(--green-dark) 245deg 360deg)}
.pie-label{font-size:2.6px;color:var(--white)}
.pie-stat{width:80px}
.pie-stat strong{display:block;font-size:10px;font-weight:400;color:var(--green-dark);margin-bottom:2px}
.pie-stat.light strong{color:var(--green-light)}
.pie-stat.grey strong{color:var(--chart-grey)}
.pie-stat p{font-size:2.3px;line-height:1.35}

/* table */
.data-table{left:18px;top:47px;width:326px;border-collapse:collapse;font-size:2.5px}
.data-table th{background:var(--green-dark);color:var(--white);font-weight:500;height:11px;line-height:1.1;border-left:.8px solid var(--white)}
.data-table th.blank{background:none}
.data-table td{height:9.5px;border-bottom:.5px solid var(--grey-line);text-align:center;color:#555}
.data-table td:first-child{text-align:left;padding-left:3px;width:98px}
.data-table td.hl{color:var(--green-dark);font-weight:500}

/* contact */
.contact-head{left:28px;top:90px;font-size:4.4px;font-weight:700;color:var(--green-dark)}
.contact-address{left:28px;top:98px;font-size:2.8px;line-height:1.3}
.contact-lines{left:28px;top:122px;font-size:2.8px;line-height:1;list-style:none}
.contact-lines li{display:flex;align-items:center;gap:3px;margin-bottom:3px}
.contact-lines svg{width:4px;height:4px}
</style>
</head>
<body>

<!-- reusable decoration -->
<svg width="0" height="0" style="position:absolute">
  <defs>
    <linearGradient id="decoDark" x1="0" y1="1" x2="1" y2="0">
      <stop offset="0" stop-color="#3d7a1c"/><stop offset="1" stop-color="#6d9f2c"/>
    </linearGradient>
    <linearGradient id="decoLight" x1="0" y1="0" x2="1" y2="1">
      <stop offset="0" stop-color="#c9dd7a"/><stop offset="1" stop-color="#a9c84a"/>
    </linearGradient>
    <symbol id="deco" viewBox="0 0 200 201">
      <circle cx="150" cy="110" r="95" fill="url(#decoDark)"/>
      <circle cx="190" cy="200" r="95" fill="url(#decoLight)" opacity=".85"/>
    </symbol>
  </defs>
</svg>

<!-- HERO COVER -->
<section class="slide hero" aria-label="Cover slide">
  <div class="brand brand-lg"><i></i>Kalvoren</div>
  <span class="brand-sub">CONSULTING</span>
  <h1 class="cover-title">Presentation<br>Title Goes Here!</h1>
  <p class="cover-subtitle">Subtitle of Presentation Goes Here</p>
  <div class="url-pill">www.kalvoren-consulting.example</div>
  <svg class="deco" role="img" aria-label="Green decorative shape"><use href="#deco"/></svg>
  <div class="copyright-strip">Copyright © Kalvoren Consulting GmbH. All Rights Reserved</div>
</section>

<!-- ROW 1 -->
<section class="slide" style="left:43px;top:858px">
  <div class="brand brand-lg"><i></i>Kalvoren</div>
  <span class="brand-sub">CONSULTING</span>
  <h1 class="cover-title">Presentation<br>Title Goes Here!</h1>
  <p class="cover-subtitle">Subtitle of Presentation Goes Here</p>
  <div class="url-pill">www.kalvoren-consulting.example</div>
  <svg class="deco" role="img" aria-label="Green decorative shape"><use href="#deco"/></svg>
  <div class="copyright-strip">Copyright © Kalvoren Consulting GmbH. All Rights Reserved</div>
</section>

<section class="slide" style="left:420px;top:858px">
  <div class="photo-field" role="img" aria-label="Soft photo of young green plants in sunlight"></div>
  <div class="brand brand-lg"><i></i>Kalvoren</div>
  <span class="brand-sub">CONSULTING</span>
  <h1 class="cover-title">Presentation<br>Title Goes Here!</h1>
  <p class="cover-subtitle">Subtitle of Presentation Goes Here</p>
  <div class="url-pill">www.kalvoren-consulting.example</div>
  <svg class="deco" role="img" aria-label="Green decorative shape" style="opacity:.9"><use href="#deco"/></svg>
  <div class="copyright-strip">Copyright © Kalvoren Consulting GmbH. All Rights Reserved</div>
</section>

<section class="slide" style="left:797px;top:858px">
  <span class="edge-accent"></span>
  <h2 class="slide-title"><b>About Us</b></h2>
  <div class="about-photo photo-leaves" role="img" aria-label="Photo of green fruit on a branch"></div>
  <div class="about-callout">Lorem ipsum dolor sit amet, consectetur adipiscing elit. Vivamus eu dui ex. Curabitur dapibus dignissim dui, in molestie metus feugiat.</div>
  <h3 class="subhead" style="left:196px;top:92px">Heading Goes Here</h3>
  <ul class="bullets" style="left:200px;top:104px;width:142px">
    <li>Lorem ipsum dolor sit amet, consectetur adipiscing elit. Vivamus eu dui ex. Curabitur dapibus dignissim dui, in molestie metus feugiat sed.</li>
    <li>Donec risus orci, gravida sit amet risus vehicula, aliquet pretium sapien. Nullam sit amet magna non ex bibendum mollis.</li>
    <li>Lorem ipsum dolor sit amet, consectetur adipiscing elit. Vivamus eu dui ex, dapibus odio varius at.</li>
  </ul>
  <div class="slide-footer"><span class="mini-brand"><i></i>Kalvoren</span><span class="footer-note">Copyright © Kalvoren Consulting GmbH. All Rights Reserved</span><span class="footer-bar"></span><span class="page-no">3</span></div>
</section>

<!-- ROW 2 -->
<section class="slide" style="left:43px;top:1078px">
  <div class="band-photo photo-landscape" role="img" aria-label="Photo of forested green hills"></div>
  <span class="edge-accent"></span>
  <h2 class="slide-title"><b>Heading</b> Goes Here</h2>
  <div class="band-box">
    <ul class="bullets on-dark">
      <li>Lorem ipsum dolor sit amet, consectetur adipiscing elit. Vivamus eu dui ex. Curabitur dapibus dignissim dui, in molestie metus feugiat sed.</li>
      <li>Duis eget tellus porta, consequat lacus vitae, venenatis dolor. Nulla facilisi. In et sollicitudin lacus. Donec risus orci, gravida sit amet risus vehicula.</li>
      <li>Nullam sit amet magna non ex bibendum mollis. Nunc vel neque eu augue dignissim congue ut vitae magna.</li>
    </ul>
  </div>
  <div class="slide-footer"><span class="mini-brand"><i></i>Kalvoren</span><span class="footer-note">Copyright © Kalvoren Consulting GmbH. All Rights Reserved</span><span class="footer-bar"></span><span class="page-no">4</span></div>
</section>

<section class="slide" style="left:420px;top:1078px">
  <span class="edge-accent"></span>
  <h2 class="slide-title"><b>Slide Title</b> Goes Here</h2>
  <div class="body-text" style="left:27px;top:60px;width:305px">
    <p>Lorem ipsum dolor sit amet, consectetur adipiscing elit. Vivamus eu dui ex. Curabitur dapibus dignissim dui, in molestie metus feugiat sed. Praesent aliquet lorem ex, eu dapibus odio varius at. Duis eget tellus porta, consequat lacus vitae, venenatis dolor. Nulla facilisi. In et sollicitudin lacus. Donec risus orci, gravida sit amet risus vehicula, aliquet pretium sapien. Nullam sit amet magna non ex bibendum mollis. Nunc vel neque eu augue dignissim congue ut vitae magna. Phasellus eget commodo arcu. Nunc vitae semper dui. Integer venenatis, tellus sit amet interdum pretium, erat neque rhoncus turpis, a aliquam augue ligula eget erat.</p>
    <p>Curabitur dapibus dignissim dui, in molestie metus feugiat sed. Praesent aliquet lorem ex, eu dapibus odio varius at. Duis eget tellus porta, consequat lacus vitae, venenatis dolor. Donec risus orci, gravida sit amet risus vehicula, aliquet pretium sapien. Nullam sit amet magna non ex bibendum mollis. Nunc vel neque eu augue dignissim congue ut vitae magna. Phasellus eget commodo arcu. Nunc vitae semper dui. Pellentesque habitant morbi tristique senectus et netus et malesuada fames.</p>
  </div>
  <div class="slide-footer"><span class="mini-brand"><i></i>Kalvoren</span><span class="footer-note">Copyright © Kalvoren Consulting GmbH. All Rights Reserved</span><span class="footer-bar"></span><span class="page-no">5</span></div>
</section>

<section class="slide" style="left:797px;top:1078px">
  <div class="team-band photo-team" role="img" aria-label="Photo of green leaves in sunlight"></div>
  <h2 class="team-title">Management <b>Team</b></h2>
  <div class="member" style="left:25px">
    <div class="portrait" role="img" aria-label="Portrait photo of team member"></div>
    <h3>Dr. Mara Feldt</h3><div class="role">Managing Partner</div>
    <p>Lorem ipsum dolor sit amet, consectetur adipiscing elit. Vivamus eu dui ex. Curabitur dapibus dignissim dui, in molestie metus feugiat sed.</p>
  </div>
  <div class="member" style="left:130px">
    <div class="portrait" role="img" aria-label="Portrait photo of team member"></div>
    <h3>Dr. Ilse Brandt</h3><div class="role">Managing Partner</div>
    <p>Lorem ipsum dolor sit amet, consectetur adipiscing elit. Vivamus eu dui ex. Curabitur dapibus dignissim dui, in molestie metus feugiat sed.</p>
  </div>
  <div class="member" style="left:235px">
    <div class="portrait" role="img" aria-label="Portrait photo of team member"></div>
    <h3>Dr. Petra Hollweg</h3><div class="role">Managing Partner</div>
    <p>Lorem ipsum dolor sit amet, consectetur adipiscing elit. Vivamus eu dui ex. Curabitur dapibus dignissim dui, in molestie metus feugiat sed.</p>
  </div>
  <div class="slide-footer"><span class="mini-brand"><i></i>Kalvoren</span><span class="footer-note">Copyright © Kalvoren Consulting GmbH. All Rights Reserved</span><span class="footer-bar"></span><span class="page-no">6</span></div>
</section>

<!-- ROW 3 -->
<section class="slide" style="left:43px;top:1298px">
  <span class="edge-accent"></span>
  <h2 class="slide-title"><b>Heading</b> Goes Here</h2>
  <div class="card dark" style="left:25px"><h3>Lorem ipsum<br>dolor sit amet</h3><p>Lorem ipsum dolor sit amet, consectetur adipiscing elit. Vivamus eu dui ex. Curabitur dapibus dignissim dui, in molestie metus feugiat sed. Praesent aliquet lorem ex, eu dapibus odio varius at. Duis eget tellus porta, consequat lacus vitae, venenatis dolor. Nulla facilisi.</p></div>
  <div class="card mid" style="left:130px"><h3>Lorem ipsum<br>dolor sit amet</h3><p>Lorem ipsum dolor sit amet, consectetur adipiscing elit. Vivamus eu dui ex. Curabitur dapibus dignissim dui, in molestie metus feugiat sed. Praesent aliquet lorem ex, eu dapibus odio varius at. Duis eget tellus porta, consequat lacus vitae, venenatis dolor. Nulla facilisi.</p></div>
  <div class="card light" style="left:236px"><h3>Lorem ipsum<br>dolor sit amet</h3><p>Lorem ipsum dolor sit amet, consectetur adipiscing elit. Vivamus eu dui ex. Curabitur dapibus dignissim dui, in molestie metus feugiat sed. Praesent aliquet lorem ex, eu dapibus odio varius at. Duis eget tellus porta, consequat lacus vitae, venenatis dolor. Nulla facilisi.</p></div>
  <div class="slide-footer"><span class="mini-brand"><i></i>Kalvoren</span><span class="footer-note">Copyright © Kalvoren Consulting GmbH. All Rights Reserved</span><span class="footer-bar"></span><span class="page-no">7</span></div>
</section>

<section class="slide" style="left:420px;top:1298px">
  <span class="edge-accent"></span>
  <h2 class="slide-title"><b>Column</b> Slide</h2>
  <h3 class="subhead" style="left:27px;top:58px">Heading Goes Here</h3>
  <ul class="bullets" style="left:29px;top:70px;width:140px">
    <li>Lorem ipsum dolor sit amet, consectetur adipiscing elit. Vivamus eu dui ex. Curabitur dapibus dignissim dui, in molestie metus feugiat sed. Praesent aliquet lorem ex, eu dapibus odio varius at.</li>
    <li>Donec risus orci, gravida sit amet risus vehicula, aliquet pretium sapien. Nullam sit amet magna non ex bibendum mollis.</li>
    <li>Nunc vitae semper dui. Integer venenatis, tellus sit amet interdum pretium, erat neque rhoncus turpis, a aliquam augue ligula eget erat.</li>
  </ul>
  <h3 class="subhead" style="left:195px;top:58px">Heading Goes Here</h3>
  <ul class="bullets" style="left:197px;top:70px;width:140px">
    <li>Lorem ipsum dolor sit amet, consectetur adipiscing elit. Vivamus eu dui ex. Curabitur dapibus dignissim dui, in molestie metus feugiat sed. Praesent aliquet lorem ex, eu dapibus odio varius at.</li>
    <li>Donec risus orci, gravida sit amet risus vehicula, aliquet pretium sapien. Nullam sit amet magna non ex bibendum mollis.</li>
    <li>Nunc vitae semper dui. Integer venenatis, tellus sit amet interdum pretium, erat neque rhoncus turpis, a aliquam augue ligula eget erat.</li>
  </ul>
  <div class="slide-footer"><span class="mini-brand"><i></i>Kalvoren</span><span class="footer-note">Copyright © Kalvoren Consulting GmbH. All Rights Reserved</span><span class="footer-bar"></span><span class="page-no">8</span></div>
</section>

<section class="slide" style="left:797px;top:1298px">
  <span class="edge-accent"></span>
  <h2 class="slide-title"><b>Timeline</b> Slide</h2>
  <span class="tl-line"></span>
  <div class="tl-item" style="left:24px"><div class="tl-year">2010</div><div class="tl-dot"></div><div class="tl-icon dark"><svg width="8" height="8" viewBox="0 0 8 8"><circle cx="4" cy="3.2" r="2.4" fill="#fff"/><rect x="3" y="5.6" width="2" height="1.6" fill="#fff"/></svg></div><h3>Heading<br>Goes Here</h3><p>Lorem ipsum dolor sit amet, consectetur adipiscing elit. Vivamus eu dui ex. Curabitur dapibus.</p></div>
  <div class="tl-item" style="left:76px"><div class="tl-year">2014</div><div class="tl-dot"></div><div class="tl-icon light"><svg width="9" height="8" viewBox="0 0 9 8"><circle cx="3" cy="2.5" r="1.5" fill="#fff"/><circle cx="6" cy="2.5" r="1.5" fill="#fff"/><path d="M0.5 7a2.5 2.5 0 0 1 5 0zM3.5 7a2.5 2.5 0 0 1 5 0z" fill="#fff"/></svg></div><h3>Heading<br>Goes Here</h3><p>Lorem ipsum dolor sit amet, consectetur adipiscing elit. Vivamus eu dui ex. Curabitur dapibus.</p></div>
  <div class="tl-item" style="left:128px"><div class="tl-year">2017</div><div class="tl-dot"></div><div class="tl-icon dark"><svg width="8" height="8" viewBox="0 0 8 8"><circle cx="3.3" cy="3.3" r="2.2" fill="none" stroke="#fff" stroke-width="1"/><path d="M5 5l2.2 2.2" stroke="#fff" stroke-width="1.2"/></svg></div><h3>Heading<br>Goes Here</h3><p>Lorem ipsum dolor sit amet, consectetur adipiscing elit. Vivamus eu dui ex. Curabitur dapibus.</p></div>
  <div class="tl-item" style="left:181px"><div class="tl-year">2018</div><div class="tl-dot"></div><div class="tl-icon light"><svg width="7" height="8" viewBox="0 0 7 8"><rect x="1" y="0.5" width="5" height="7" fill="#fff"/><path d="M2 3h3M2 4.5h3M2 6h2" stroke="#a9c84a" stroke-width=".6"/></svg></div><h3>Heading<br>Goes Here</h3><p>Lorem ipsum dolor sit amet, consectetur adipiscing elit. Vivamus eu dui ex. Curabitur dapibus.</p></div>
  <div class="tl-item" style="left:233px"><div class="tl-year">2020</div><div class="tl-dot"></div><div class="tl-icon dark"><svg width="8" height="8" viewBox="0 0 8 8"><circle cx="4" cy="4" r="2.6" fill="none" stroke="#fff" stroke-width="1.6" stroke-dasharray="1.2 .8"/><circle cx="4" cy="4" r="1" fill="#fff"/></svg></div><h3>Heading<br>Goes Here</h3><p>Lorem ipsum dolor sit amet, consectetur adipiscing elit. Vivamus eu dui ex. Curabitur dapibus.</p></div>
  <div class="tl-item" style="left:286px"><div class="tl-year">2023</div><div class="tl-dot"></div><div class="tl-icon light"><svg width="8" height="8" viewBox="0 0 8 8"><rect x="1" y="5" width="1.4" height="2.5" fill="#fff"/><rect x="3.3" y="3.5" width="1.4" height="4" fill="#fff"/><rect x="5.6" y="1.5" width="1.4" height="6" fill="#fff"/></svg></div><h3>Heading<br>Goes Here</h3><p>Lorem ipsum dolor sit amet, consectetur adipiscing elit. Vivamus eu dui ex. Curabitur dapibus.</p></div>
  <div class="slide-footer"><span class="mini-brand"><i></i>Kalvoren</span><span class="footer-note">Copyright © Kalvoren Consulting GmbH. All Rights Reserved</span><span class="footer-bar"></span><span class="page-no">9</span></div>
</section>

<!-- ROW 4 -->
<section class="slide" style="left:43px;top:1518px">
  <span class="edge-accent"></span>
  <h2 class="slide-title"><b>Timeline</b> Slide</h2>
  <span class="tl-line"></span>
  <div class="tl-item" style="left:24px"><div class="tl-year">2010</div><div class="tl-dot"></div><div class="tl-icon dark ring"><svg width="8" height="8" viewBox="0 0 8 8"><circle cx="4" cy="3.2" r="2.4" fill="#fff"/><rect x="3" y="5.6" width="2" height="1.6" fill="#fff"/></svg></div><h3>Heading<br>Goes Here</h3><p>Lorem ipsum dolor sit amet, consectetur adipiscing elit. Vivamus eu dui ex. Curabitur dapibus.</p></div>
  <div class="tl-item" style="left:76px"><div class="tl-year">2014</div><div class="tl-dot"></div><div class="tl-icon light ring"><svg width="9" height="8" viewBox="0 0 9 8"><circle cx="3" cy="2.5" r="1.5" fill="#fff"/><circle cx="6" cy="2.5" r="1.5" fill="#fff"/><path d="M0.5 7a2.5 2.5 0 0 1 5 0zM3.5 7a2.5 2.5 0 0 1 5 0z" fill="#fff"/></svg></div><h3>Heading<br>Goes Here</h3><p>Lorem ipsum dolor sit amet, consectetur adipiscing elit. Vivamus eu dui ex. Curabitur dapibus.</p></div>
  <div class="tl-item" style="left:128px"><div class="tl-year">2017</div><div class="tl-dot"></div><div class="tl-icon dark ring"><svg width="8" height="8" viewBox="0 0 8 8"><circle cx="3.3" cy="3.3" r="2.2" fill="none" stroke="#fff" stroke-width="1"/><path d="M5 5l2.2 2.2" stroke="#fff" stroke-width="1.2"/></svg></div><h3>Heading<br>Goes Here</h3><p>Lorem ipsum dolor sit amet, consectetur adipiscing elit. Vivamus eu dui ex. Curabitur dapibus.</p></div>
  <div class="tl-item" style="left:181px"><div class="tl-year">2018</div><div class="tl-dot"></div><div class="tl-icon light ring"><svg width="7" height="8" viewBox="0 0 7 8"><rect x="1" y="0.5" width="5" height="7" fill="#fff"/><path d="M2 3h3M2 4.5h3M2 6h2" stroke="#a9c84a" stroke-width=".6"/></svg></div><h3>Heading<br>Goes Here</h3><p>Lorem ipsum dolor sit amet, consectetur adipiscing elit. Vivamus eu dui ex. Curabitur dapibus.</p></div>
  <div class="tl-item" style="left:233px"><div class="tl-year">2020</div><div class="tl-dot"></div><div class="tl-icon dark ring"><svg width="8" height="8" viewBox="0 0 8 8"><circle cx="4" cy="4" r="2.6" fill="none" stroke="#fff" stroke-width="1.6" stroke-dasharray="1.2 .8"/><circle cx="4" cy="4" r="1" fill="#fff"/></svg></div><h3>Heading<br>Goes Here</h3><p>Lorem ipsum dolor sit amet, consectetur adipiscing elit. Vivamus eu dui ex. Curabitur dapibus.</p></div>
  <div class="tl-item" style="left:286px"><div class="tl-year">2023</div><div class="tl-dot"></div><div class="tl-icon light ring"><svg width="8" height="8" viewBox="0 0 8 8"><rect x="1" y="5" width="1.4" height="2.5" fill="#fff"/><rect x="3.3" y="3.5" width="1.4" height="4" fill="#fff"/><rect x="5.6" y="1.5" width="1.4" height="6" fill="#fff"/></svg></div><h3>Heading<br>Goes Here</h3><p>Lorem ipsum dolor sit amet, consectetur adipiscing elit. Vivamus eu dui ex. Curabitur dapibus.</p></div>
  <div class="slide-footer"><span class="mini-brand"><i></i>Kalvoren</span><span class="footer-note">Copyright © Kalvoren Consulting GmbH. All Rights Reserved</span><span class="footer-bar"></span><span class="page-no">10</span></div>
</section>

<section class="slide" style="left:420px;top:1518px">
  <h2 class="section-title">Section Break</h2>
  <p class="section-text">Lorem ipsum dolor sit amet, consectetur adipiscing elit. Vivamus eu dui ex. Curabitur dapibus dignissim dui, in molestie metus feugiat sed. Praesent aliquet lorem ex.</p>
  <svg class="deco" role="img" aria-label="Green decorative shape"><use href="#deco"/></svg>
</section>

<section class="slide" style="left:797px;top:1518px">
  <div class="photo-field" role="img" aria-label="Soft photo of young green plants in sunlight"></div>
  <h2 class="section-title">Section Break</h2>
  <p class="section-text">Lorem ipsum dolor sit amet, consectetur adipiscing elit. Vivamus eu dui ex. Curabitur dapibus dignissim dui, in molestie metus feugiat sed. Praesent aliquet lorem ex.</p>
  <svg class="deco" role="img" aria-label="Green decorative shape" style="opacity:.9"><use href="#deco"/></svg>
</section>

<!-- ROW 5 -->
<section class="slide" style="left:43px;top:1739px">
  <span class="edge-accent"></span>
  <h2 class="slide-title"><b>Pie Chart</b> Slide</h2>
  <div class="donut" style="left:40px">
    <svg viewBox="0 0 48 48"><circle cx="24" cy="24" r="19" fill="none" stroke="#e6e6e6" stroke-width="6"/><circle cx="24" cy="24" r="19" fill="none" stroke="#3d7a1c" stroke-width="6" stroke-dasharray="41.8 119.4" transform="rotate(-90 24 24)"/><text x="24" y="27" text-anchor="middle" font-size="9" fill="#3d7a1c" font-family="Alegreya Sans,sans-serif">35%</text></svg>
    <h3>Heading Goes Here</h3><p>Lorem ipsum dolor sit amet, consectetur adipiscing elit. Vivamus eu dui ex. Curabitur dapibus dignissim dui.</p>
  </div>
  <div class="donut" style="left:140px">
    <svg viewBox="0 0 48 48"><circle cx="24" cy="24" r="19" fill="none" stroke="#ececec" stroke-width="6"/><circle cx="24" cy="24" r="19" fill="none" stroke="#c6dc75" stroke-width="6" stroke-dasharray="77.6 119.4" transform="rotate(-90 24 24)"/><text x="24" y="27" text-anchor="middle" font-size="9" fill="#a9c84a" font-family="Alegreya Sans,sans-serif">65%</text></svg>
    <h3 style="color:var(--green-light)">Heading Goes Here</h3><p>Lorem ipsum dolor sit amet, consectetur adipiscing elit. Vivamus eu dui ex. Curabitur dapibus dignissim dui.</p>
  </div>
  <div class="donut" style="left:240px">
    <svg viewBox="0 0 48 48"><circle cx="24" cy="24" r="19" fill="none" stroke="#e6e6e6" stroke-width="6"/><circle cx="24" cy="24" r="19" fill="none" stroke="#6d7072" stroke-width="6" stroke-dasharray="101.5 119.4" transform="rotate(-90 24 24)"/><text x="24" y="27" text-anchor="middle" font-size="9" fill="#6d7072" font-family="Alegreya Sans,sans-serif">85%</text></svg>
    <h3 style="color:var(--chart-grey)">Heading Goes Here</h3><p>Lorem ipsum dolor sit amet, consectetur adipiscing elit. Vivamus eu dui ex. Curabitur dapibus dignissim dui.</p>
  </div>
  <div class="slide-footer"><span class="mini-brand"><i></i>Kalvoren</span><span class="footer-note">Copyright © Kalvoren Consulting GmbH. All Rights Reserved</span><span class="footer-bar"></span><span class="page-no">13</span></div>
</section>

<section class="slide" style="left:420px;top:1739px">
  <span class="edge-accent"></span>
  <h2 class="slide-title"><b>Column Chart</b> Slide</h2>
  <div class="bar-chart" style="left:22px">
    <div class="bar-row"><span>Category 4</span><i class="seg a" style="width:28px"></i><i class="seg b" style="width:22px"></i><i class="seg c" style="width:34px"></i></div>
    <div class="bar-row"><span>Category 3</span><i class="seg a" style="width:26px"></i><i class="seg b" style="width:12px"></i><i class="seg c" style="width:28px"></i></div>
    <div class="bar-row"><span>Category 2</span><i class="seg a" style="width:18px"></i><i class="seg b" style="width:34px"></i><i class="seg c" style="width:14px"></i></div>
    <div class="bar-row"><span>Category 1</span><i class="seg a" style="width:30px"></i><i class="seg b" style="width:26px"></i><i class="seg c" style="width:10px"></i></div>
    <div class="bar-axis"><i>0</i><i>2</i><i>4</i><i>6</i><i>8</i><i>10</i><i>12</i><i>14</i></div>
  </div>
  <div class="bar-chart" style="left:182px">
    <div class="bar-row"><span>Category 4</span><i class="seg a" style="width:24px"></i><i class="seg b" style="width:30px"></i><i class="seg c" style="width:10px"></i></div>
    <div class="bar-row"><span>Category 3</span><i class="seg a" style="width:20px"></i><i class="seg b" style="width:60px"></i><i class="seg c" style="width:14px"></i></div>
    <div class="bar-row"><span>Category 2</span><i class="seg a" style="width:28px"></i><i class="seg b" style="width:44px"></i><i class="seg c" style="width:10px"></i></div>
    <div class="bar-row"><span>Category 1</span><i class="seg a" style="width:30px"></i><i class="seg b" style="width:40px"></i><i class="seg c" style="width:12px"></i></div>
    <div class="bar-axis"><i>0</i><i>5</i><i>10</i><i>15</i><i>20</i></div>
  </div>
  <div class="chart-note" style="left:28px"><h3>Heading Goes Here</h3><p class="body-text" style="position:static;font-size:2.4px">Nullam sit amet magna non ex bibendum mollis. Nunc vel neque eu augue dignissim congue ut vitae magna. Phasellus eget commodo arcu.</p></div>
  <div class="chart-note" style="left:188px"><h3>Heading Goes Here</h3><p class="body-text" style="position:static;font-size:2.4px">Nullam sit amet magna non ex bibendum mollis. Nunc vel neque eu augue dignissim congue ut vitae magna. Phasellus eget commodo arcu.</p></div>
  <div class="slide-footer"><span class="mini-brand"><i></i>Kalvoren</span><span class="footer-note">Copyright © Kalvoren Consulting GmbH. All Rights Reserved</span><span class="footer-bar"></span><span class="page-no">14</span></div>
</section>

<section class="slide" style="left:797px;top:1739px">
  <span class="edge-accent"></span>
  <h2 class="slide-title"><b>Pie Chart</b> Slide</h2>
  <div class="pie-stat" style="left:25px;top:58px"><strong>25%</strong><p>Nunc placerat, arcu nec mattis fermentum, nisi mauris convallis nunc, ut luctus nunc nisl id ex.</p></div>
  <div class="pie-stat grey" style="left:25px;top:113px"><strong>12%</strong><p>Nunc placerat, arcu nec mattis fermentum, nisi mauris convallis nunc, ut luctus nunc nisl id ex.</p></div>
  <div class="pie-stat" style="left:258px;top:58px"><strong>20%</strong><p>Nunc placerat, arcu nec mattis fermentum, nisi mauris convallis nunc, ut luctus nunc nisl id ex.</p></div>
  <div class="pie-stat light" style="left:258px;top:113px"><strong>36%</strong><p>Nunc placerat, arcu nec mattis fermentum, nisi mauris convallis nunc, ut luctus nunc nisl id ex.</p></div>
  <div class="pie-wrap">
    <div class="pie-side"></div>
    <div class="pie-top"></div>
    <span class="pie-label" style="position:absolute;left:34px;top:14px">25%</span>
    <span class="pie-label" style="position:absolute;left:88px;top:12px">20%</span>
    <span class="pie-label" style="position:absolute;left:10px;top:36px">12%</span>
    <span class="pie-label" style="position:absolute;left:95px;top:40px">36%</span>
  </div>
  <div class="slide-footer"><span class="mini-brand"><i></i>Kalvoren</span><span class="footer-note">Copyright © Kalvoren Consulting GmbH. All Rights Reserved</span><span class="footer-bar"></span><span class="page-no">15</span></div>
</section>

<!-- ROW 6 -->
<section class="slide" style="left:43px;top:1959px">
  <span class="edge-accent"></span>
  <h2 class="slide-title"><b>Table</b>/Data Slide</h2>
  <table class="data-table">
    <thead><tr><th class="blank"></th><th>Lorem ipsum<br>amet, consectetur</th><th>Lorem ipsum<br>amet, consectetur</th><th>Lorem ipsum<br>amet, consectetur</th><th>Lorem ipsum<br>amet, consectetur</th></tr></thead>
    <tbody>
      <tr><td>Lorem ipsum dolor sit amet</td><td class="hl">Text Goes Here</td><td>Text Goes Here</td><td>Text Goes Here</td><td>Text Goes Here</td></tr>
      <tr><td>Pellentesque habitant morbi tristique</td><td class="hl">Text Goes Here</td><td>Text Goes Here</td><td>Text Goes Here</td><td>Text Goes Here</td></tr>
      <tr><td>Nullam sit amet magna non ex</td><td class="hl">Text Goes Here</td><td>Text Goes Here</td><td>Text Goes Here</td><td>Text Goes Here</td></tr>
      <tr><td>Vivamus eu dui ex</td><td class="hl">Text Goes Here</td><td>Text Goes Here</td><td>Text Goes Here</td><td>Text Goes Here</td></tr>
      <tr><td>Donec risus orci, gravida sit amet</td><td class="hl">Text Goes Here</td><td>Text Goes Here</td><td>Text Goes Here</td><td>Text Goes Here</td></tr>
      <tr><td>Nulla facilisi. In et sollicitudin lacus</td><td class="hl">Text Goes Here</td><td>Text Goes Here</td><td>Text Goes Here</td><td>Text Goes Here</td></tr>
      <tr><td>Nunc vel neque eu augue dignissim</td><td class="hl">Text Goes Here</td><td>Text Goes Here</td><td>Text Goes Here</td><td>Text Goes Here</td></tr>
    </tbody>
  </table>
  <div class="slide-footer"><span class="mini-brand"><i></i>Kalvoren</span><span class="footer-note">Copyright © Kalvoren Consulting GmbH. All Rights Reserved</span><span class="footer-bar"></span><span class="page-no">16</span></div>
</section>

<section class="slide" style="left:420px;top:1959px">
  <div class="brand brand-lg" style="top:50px"><i></i>Kalvoren</div>
  <span class="brand-sub" style="top:65px">CONSULTING</span>
  <h3 class="contact-head">Contact Us</h3>
  <p class="contact-address">Nachhaltigkeitsberatung<br>Lindenhof Business Park<br>Auenweg 12<br>60311 Frankfurt a. M.</p>
  <ul class="contact-lines">
    <li><svg viewBox="0 0 8 8"><path d="M1.5 1h2l.8 2-1.2.8a4.5 4.5 0 0 0 2.1 2.1l.8-1.2 2 .8v2A6.5 6.5 0 0 1 1.5 1z" fill="#3d7a1c"/></svg>+49 (0) 000 – 555 0142</li>
    <li><svg viewBox="0 0 8 8"><rect x=".5" y="1.5" width="7" height="5" fill="none" stroke="#3d7a1c" stroke-width=".9"/><path d="M.5 1.5l3.5 3 3.5-3" fill="none" stroke="#3d7a1c" stroke-width=".9"/></svg>info@kalvoren-consulting.example</li>
    <li><svg viewBox="0 0 8 8"><circle cx="4" cy="4" r="3.3" fill="none" stroke="#3d7a1c" stroke-width=".8"/><path d="M.7 4h6.6M4 .7c-2 2-2 4.6 0 6.6M4 .7c2 2 2 4.6 0 6.6" fill="none" stroke="#3d7a1c" stroke-width=".6"/></svg>www.kalvoren-consulting.example</li>
  </ul>
  <svg class="deco" role="img" aria-label="Green decorative shape"><use href="#deco"/></svg>
  <div class="copyright-strip">Copyright © Kalvoren Consulting GmbH. All Rights Reserved</div>
</section>

<section class="slide" style="left:797px;top:1959px">
  <div class="photo-field" role="img" aria-label="Soft photo of young green plants in sunlight"></div>
  <div class="brand brand-lg" style="top:50px"><i></i>Kalvoren</div>
  <span class="brand-sub" style="top:65px">CONSULTING</span>
  <h3 class="contact-head">Contact Us</h3>
  <p class="contact-address">Nachhaltigkeitsberatung<br>Lindenhof Business Park<br>Auenweg 12<br>60311 Frankfurt a. M.</p>
  <ul class="contact-lines">
    <li><svg viewBox="0 0 8 8"><path d="M1.5 1h2l.8 2-1.2.8a4.5 4.5 0 0 0 2.1 2.1l.8-1.2 2 .8v2A6.5 6.5 0 0 1 1.5 1z" fill="#3d7a1c"/></svg>+49 (0) 000 – 555 0142</li>
    <li><svg viewBox="0 0 8 8"><rect x=".5" y="1.5" width="7" height="5" fill="none" stroke="#3d7a1c" stroke-width=".9"/><path d="M.5 1.5l3.5 3 3.5-3" fill="none" stroke="#3d7a1c" stroke-width=".9"/></svg>info@kalvoren-consulting.example</li>
    <li><svg viewBox="0 0 8 8"><circle cx="4" cy="4" r="3.3" fill="none" stroke="#3d7a1c" stroke-width=".8"/><path d="M.7 4h6.6M4 .7c-2 2-2 4.6 0 6.6M4 .7c2 2 2 4.6 0 6.6" fill="none" stroke="#3d7a1c" stroke-width=".6"/></svg>www.kalvoren-consulting.example</li>
  </ul>
  <svg class="deco" role="img" aria-label="Green decorative shape" style="opacity:.9"><use href="#deco"/></svg>
  <div class="copyright-strip">Copyright © Kalvoren Consulting GmbH. All Rights Reserved</div>
</section>

</body>
</html>
```